Company or website name
- Wandering Maple Journeys
- Links to the website
- http://wanderingmaplejourneys.example/
- Describe your company and organization and target audience
- This is a website for people to follow my travels. It will humorously cover topics that randomly come to me as I travel abroad and show pictures as well as \'articles\' that describe what I encounter.
- The design should have the following
- I would like this website to be easy for me to post my blogs / articles as well as pictures. I want twitter, facebook and google+ widgets to be an option to add as well. I am pretty open...I just want it to be clean, simple showcase the logo and not be too complicated to make simple changes.
- Other Facts

```html
<!DOCTYPE html>
<html lang="en">
<head>
<meta charset="utf-8">
<title>Wandering Maple Journeys – My blog</title>
<link rel="stylesheet" href="https://fonts.googleapis.com/css2?family=Comfortaa:wght@500;700&family=Arimo:wght@400;700&display=swap">
<style>
  :root{
    --pink:#fb3a9e;
    --pink-deep:#f0288f;
    --sky:#4fc3f0;
    --date:#45c6f5;
    --white:#ffffff;
    --night:#0f1d3d;
  }
  html,body{margin:0;padding:0;overflow:hidden;}
  body{width:1200px;height:1146px;position:relative;background:var(--pink);font-family:'Comfortaa',sans-serif;}
  a{text-decoration:none;}
  .hero{position:absolute;left:0;top:0;width:1200px;height:842px;
    background:linear-gradient(180deg,#0d1a3a 0%,#2b4d86 14%,#7d9bc6 24%,#b9855a 32%,#9c5c36 42%,#6f6a67 58%,#3c3b3d 75%,#2a2a2c 100%);}
  .footer{position:absolute;left:0;top:842px;width:1200px;height:304px;background:var(--pink);}
  .brand{position:absolute;left:0;top:0;width:206px;height:122px;background:#f74bd9;display:flex;align-items:center;gap:8px;padding:0 10px;box-sizing:border-box;}
  .brand-dot{width:30px;height:30px;border-radius:50%;background:var(--night);flex:none;}
  .brand-name{font-weight:700;font-size:18px;line-height:1.15;color:var(--night);}
  .nav{position:absolute;top:0;left:0;}
  .nav-heart{position:absolute;left:588px;top:8px;width:110px;height:94px;}
  .nav-current{position:absolute;left:588px;top:38px;width:108px;text-align:center;color:var(--white);font-weight:700;font-size:21px;white-space:nowrap;}
  .nav-link{position:absolute;top:44px;color:var(--pink);font-weight:700;font-size:23px;white-space:nowrap;}
  .panel{position:absolute;left:403px;top:82px;width:774px;height:856px;background:var(--white);border-radius:18px;}
  .date{position:absolute;width:96px;height:96px;border-radius:50%;background:var(--date);color:var(--white);font-weight:700;font-size:21px;text-align:center;line-height:34px;display:flex;flex-direction:column;justify-content:center;}
  .post-title{position:absolute;left:437px;margin:0;font-family:'Arimo',sans-serif;font-weight:400;font-size:27px;color:var(--sky);white-space:nowrap;}
  .post-image{position:absolute;left:423px;width:526px;}
  .post-text{position:absolute;left:425px;width:496px;margin:0;font-family:'Arimo',sans-serif;font-size:11.5px;line-height:16px;color:var(--sky);}
  .comments{position:absolute;left:843px;width:105px;height:31px;border-radius:16px;background:var(--pink-deep);color:var(--white);font-family:'Arimo',sans-serif;font-weight:700;font-size:12px;display:flex;align-items:center;justify-content:center;}
  .divider{position:absolute;left:425px;top:396px;width:522px;height:1px;background:linear-gradient(90deg,#f3d2e4,#f7a3cc,#e9e9e9);}
  .older{position:absolute;left:424px;top:900px;font-family:'Arimo',sans-serif;font-weight:700;font-size:10.5px;color:var(--pink-deep);}
  .side-feature{position:absolute;left:965px;top:100px;width:228px;height:288px;box-sizing:border-box;border:6px solid var(--pink-deep);border-radius:4px;
    background:linear-gradient(180deg,#12224f 0%,#1f3c78 40%,#2e9ed6 70%,#1a6fbf 100%);}
  .recent-heading{position:absolute;left:62px;top:916px;margin:0;color:var(--white);font-weight:700;font-size:17px;}
  .recent-list{position:absolute;left:62px;top:948px;width:500px;margin:0;padding:0;list-style:none;border-top:2px dashed rgba(255,255,255,.85);}
  .recent-list li{height:51px;border-bottom:2px dashed rgba(255,255,255,.85);display:flex;justify-content:space-between;align-items:center;color:var(--white);}
  .recent-title{font-weight:700;font-size:17px;white-space:nowrap;}
  .recent-date{font-weight:700;font-size:11px;white-space:nowrap;}
  .follow{position:absolute;left:933px;top:964px;color:var(--white);font-weight:700;font-size:20px;white-space:nowrap;}
  .social{position:absolute;width:42px;height:42px;border-radius:5px;}
</style>
</head>
<body>
  <div class="hero" role="img" aria-label="Background photograph of a winding desert road under a blue sky"></div>
  <div class="footer"></div>

  <a class="brand" href="http://wanderingmaplejourneys.example/">
    <span class="brand-dot"></span>
    <span class="brand-name">Wandering Maple Journeys</span>
  </a>

  <nav class="nav">
    <svg class="nav-heart" viewBox="0 0 110 94" aria-hidden="true">
      <path d="M55 92 C30 78 2 60 2 32 C2 14 16 2 32 2 C44 2 52 9 55 16 C58 9 66 2 78 2 C94 2 108 14 108 32 C108 60 80 78 55 92Z" fill="#fb3a9e"/>
    </svg>
    <span class="nav-current">My blog</span>
    <span class="nav-link" style="left:712px">My Tours</span>
    <span class="nav-link" style="left:850px">Photos</span>
    <span class="nav-link" style="left:956px">Places</span>
    <span class="nav-link" style="left:1048px">Contact</span>
  </nav>

  <main class="panel"></main>

  <article>
    <div class="date" style="left:322px;top:106px"><span>jAN</span><span>15</span></div>
    <h2 class="post-title" style="top:131px">Lorem ipsum dolor sit amet</h2>
    <div class="post-image" role="img" aria-label="Photo of a red train crossing green alpine meadows below snowy mountains" style="top:176px;height:205px;background:linear-gradient(180deg,#6b88b4 0%,#c9d3df 25%,#6d6f66 45%,#8fa64a 65%,#a9b845 100%);"></div>
    <div class="divider"></div>
    <p class="post-text" style="top:412px">Lorem ipsum dolor sit amet, consectetuer adipiscing elit, sed diam nonummy nibh euismod tincidunt ut laoreet dolore magna aliquam erat volutpat.</p>
    <div class="comments" style="top:456px">(0 comments)</div>
  </article>

  <article>
    <div class="date" style="left:325px;top:500px"><span>jAN</span><span>14</span></div>
    <h2 class="post-title" style="top:524px">Set ipsum dolor sit amet</h2>
    <div class="post-image" role="img" aria-label="Photo of letter tiles spelling a travel wish laid on a world map" style="top:571px;height:225px;background:linear-gradient(135deg,#bcd9ee 0%,#e8ecef 35%,#b7d8ea 60%,#9fc6e2 100%);"></div>
    <p class="post-text" style="top:806px">Lorem ipsum dolor sit amet, consectetuer adipiscing elit, sed diam nonummy nibh euismod tincidunt ut laoreet dolore magna aliquam erat volutpat.</p>
    <div class="comments" style="top:850px">(0 comments)</div>
  </article>

  <a class="older" href="#">Older Entries</a>

  <aside class="side-feature" role="img" aria-label="Illustration of world landmarks on a globe with an airplane and the moon"></aside>

  <section>
    <h3 class="recent-heading">RECENT POSTS</h3>
    <ul class="recent-list">
      <li><span class="recent-title">Lorem ipsum dolor sit amet</span><span class="recent-date">14th jan 2014</span></li>
      <li><span class="recent-title">Set ipsum dolor sit amet</span><span class="recent-date">15th jan 2014</span></li>
      <li><span class="recent-title">Phasellus commodo placerat eros</span><span class="recent-date">15th jan 2014</span></li>
    </ul>
  </section>

  <section>
    <div class="follow">Follow us on :</div>
    <a class="social" href="#" aria-label="Social profile 1" style="left:1027px;top:1007px;background:#3b5a9a"></a>
    <a class="social" href="#" aria-label="Social profile 2" style="left:1096px;top:1007px;background:#1f7bc1"></a>
    <a class="social" href="#" aria-label="Social profile 3" style="left:1027px;top:1069px;background:#5ec4ef"></a>
    <a class="social" href="#" aria-label="Social profile 4" style="left:1096px;top:1069px;background:#f2f2f2"></a>
  </section>
</body>
</html>
```